Business Card Design and stationary (thank you cards)

I am basically starting a "handyman" business but have a little ego issue with that term. I have been a professional in the design and construction business for 30 years. I want simple…I will define the scope of work I do as i move forward, and it can vary and i want it to vary.

Target Market(s)

Homeowners mostly

Industry/Entity Type

Business

Contact Information for Business Card

Company Name is "Tidy Corner Crew" Dale P. Whitcombe, 42 Larkvale Hollow Road, Harrowmere, Vt, 06419 (but I may want to use a PO Box), Phone is 860-555-0187, email is dwhitcombe584@mailnest.example,

Font styles to use
Sans Serif

Requirements
Should not have
• anything pre designed….hammers or whatever…custom lines to make home features as shone but simple and elegant

```html
<!DOCTYPE html>
<html lang="en">
<head>
<meta charset="utf-8">
<title>Tidy Corner Crew – Business Card</title>
<link href="https://fonts.googleapis.com/css2?family=Arimo:wght@400;700&family=Roboto+Condensed:wght@400;700&display=swap" rel="stylesheet">
<style>
  :root {
    --brand-blue: #2a4fa4;
    --brand-green: #4cbf35;
    --page: #ffffff;
    --silver-dark: #c9cbcc;
    --silver-mid: #e9eaea;
    --silver-light: #ffffff;
    --ruler-light: #f7f7f7;
    --ruler-shade: #d4d5d6;
  }
  * { box-sizing: border-box; margin: 0; padding: 0; }
  html, body {
    width: 1006px;
    height: 1200px;
    overflow: hidden;
    background: var(--page);
  }
  .canvas {
    position: relative;
    width: 1006px;
    height: 1200px;
  }
  .card {
    position: absolute;
    width: 780px;
    height: 461px;
    overflow: hidden;
    background: linear-gradient(90deg, var(--silver-dark) 0%, var(--silver-mid) 30%, var(--silver-light) 62%, var(--silver-mid) 88%, var(--silver-dark) 100%);
    box-shadow: 0 0 18px rgba(0,0,0,0.35);
  }
  .card--front { left: 113px; top: 104px; }
  .card--back  { left: 106px; top: 656px; }

  .ruler-band {
    position: absolute;
    left: 0;
    top: 0;
    width: 780px;
    height: 461px;
  }

  .brand {
    position: absolute;
    font-family: "Arimo", Arial, sans-serif;
    color: var(--brand-blue);
    white-space: nowrap;
  }
  .brand__name {
    display: block;
    font-weight: 700;
  }
  .brand__tagline {
    display: block;
    font-weight: 400;
  }
  .card--front .brand { left: 190px; top: 218px; }
  .card--front .brand__name { font-size: 54px; letter-spacing: -0.5px; line-height: 1; }
  .card--front .brand__tagline { font-size: 22px; margin-top: 22px; }

  .card--back .brand { right: 42px; top: 116px; text-align: left; }
  .card--back .brand__name { font-size: 27px; line-height: 1; }
  .card--back .brand__tagline { font-size: 12px; margin-top: 10px; }

  .contact {
    position: absolute;
    left: 222px;
    top: 208px;
    font-family: "Roboto Condensed", "Arial Narrow", sans-serif;
    color: var(--brand-blue);
  }
  .contact__name {
    font-size: 26px;
    font-weight: 700;
    margin-bottom: 18px;
  }
  .contact__list { list-style: none; }
  .contact__item {
    display: flex;
    align-items: center;
    font-size: 25px;
    height: 28px;
    margin-bottom: 13px;
    white-space: nowrap;
  }
  .contact__item:nth-child(3) { margin-top: 4px; }
  .contact__icon {
    width: 22px;
    height: 22px;
    margin-right: 14px;
    flex: none;
  }
</style>
</head>
<body>
<main class="canvas">

  <section class="card card--front" aria-label="Business card front">
    <svg class="ruler-band" viewBox="0 0 780 461" role="img" aria-label="Diagonal measuring ruler illustration across the top-left corner">
      <defs>
        <linearGradient id="rulerFront" x1="0" y1="1" x2="1" y2="0">
          <stop offset="0" stop-color="var(--ruler-shade)"/>
          <stop offset="0.5" stop-color="var(--ruler-light)"/>
          <stop offset="1" stop-color="var(--ruler-shade)"/>
        </linearGradient>
      </defs>
      <polygon points="0,262 318,0 420,0 0,350" fill="url(#rulerFront)" opacity="0.85"/>
    </svg>
    <div class="brand">
      <span class="brand__name">Tidy Corner Crew</span>
      <span class="brand__tagline">Professional Handyman</span>
    </div>
  </section>

  <section class="card card--back" aria-label="Business card back">
    <svg class="ruler-band" viewBox="0 0 780 461" role="img" aria-label="Diagonal measuring ruler illustration across the top-left corner">
      <defs>
        <linearGradient id="rulerBack" x1="0" y1="1" x2="1" y2="0">
          <stop offset="0" stop-color="var(--ruler-shade)"/>
          <stop offset="0.5" stop-color="var(--ruler-light)"/>
          <stop offset="1" stop-color="var(--ruler-shade)"/>
        </linearGradient>
      </defs>
      <polygon points="0,262 318,0 420,0 0,350" fill="url(#rulerBack)" opacity="0.85"/>
    </svg>

    <div class="brand">
      <span class="brand__name">Tidy Corner Crew</span>
      <span class="brand__tagline">Professional Handyman</span>
    </div>

    <div class="contact">
      <p class="contact__name">Dale P. Whitcombe</p>
      <ul class="contact__list">
        <li class="contact__item">
          <svg class="contact__icon" viewBox="0 0 22 22" aria-hidden="true">
            <rect x="5" y="1.5" width="12" height="19" rx="2" fill="none" stroke="var(--brand-green)" stroke-width="2"/>
            <line x1="9" y1="17" x2="13" y2="17" stroke="var(--brand-green)" stroke-width="1.6"/>
          </svg>
          555 555 0187
        </li>
        <li class="contact__item">
          <svg class="contact__icon" viewBox="0 0 22 22" aria-hidden="true">
            <rect x="1.5" y="5" width="19" height="12" fill="none" stroke="var(--brand-green)" stroke-width="2"/>
            <polyline points="1.5,5 11,12 20.5,5" fill="none" stroke="var(--brand-green)" stroke-width="1.8"/>
          </svg>
          dwhitcombe584@mailnest.example
        </li>
        <li class="contact__item">
          <svg class="contact__icon" viewBox="0 0 22 22" aria-hidden="true">
            <polygon points="11,2 21,9 1,9" fill="var(--brand-green)"/>
            <rect x="3" y="10" width="16" height="10" fill="none" stroke="var(--brand-green)" stroke-width="2"/>
            <rect x="9" y="12" width="4" height="8" fill="var(--brand-green)"/>
          </svg>
          42 Larkvale Hollow Road, Harrowmere, Vt, 06419
        </li>
      </ul>
    </div>
  </section>

</main>
</body>
</html>
```